Korvell Plant Services

We are a heavy diesel mechanical business with additional air con certificates, remapping engine rebuilt

Contact Information for Business Card

Company Name, Director Name, Managing Director, Contact details, email and website

Font styles to use
Serif
Script

```html
<!DOCTYPE html>
<html lang="en">
<head>
<meta charset="utf-8">
<title>Korvell Plant Services – Business Card</title>
<link href="https://fonts.googleapis.com/css2?family=Source+Serif+4:wght@400;600&display=swap" rel="stylesheet">
<style>
  :root {
    --backdrop: #feeca5;
    --card-white: #ffffff;
    --navy: #06066a;
    --ink: #1a1a1a;
  }
  * { margin: 0; padding: 0; box-sizing: border-box; }
  html, body {
    width: 1200px; height: 1200px; overflow: hidden;
    background: var(--backdrop);
    font-family: "Source Serif 4", Georgia, serif;
  }
  .canvas { position: relative; width: 1200px; height: 1200px; }
  .card {
    position: absolute; left: 159px; width: 882px; height: 504px;
  }
  .card--front { top: 66px; background: var(--card-white); }
  .card--back { top: 636px; background: var(--navy); }

  .brand-name {
    position: absolute;
    font-weight: 600;
    line-height: 1;
    text-align: center;
  }
  .card--front .brand-name { left: 130px; top: 205px; width: 260px; color: var(--navy); }
  .brand-name__main { display: block; font-size: 52px; letter-spacing: 0.5px; }
  .brand-name__sub { display: block; font-size: 22px; margin-top: 8px; }

  .divider {
    position: absolute; left: 415px; top: 165px;
    width: 1.5px; height: 173px; background: var(--ink);
  }

  .contact-block { position: absolute; left: 442px; top: 160px; }
  .person-name {
    font-size: 37px; font-weight: 600; color: var(--navy); line-height: 1;
  }
  .person-role {
    font-size: 17px; color: var(--ink); margin-top: 8px;
  }
  .contact-list { list-style: none; margin-top: 22px; }
  .contact-item {
    display: flex; align-items: center; height: 31.5px;
    font-size: 17px; color: var(--ink);
  }
  .contact-icon { width: 24px; height: 24px; margin-right: 12px; fill: var(--navy); }

  .card--back .brand-name { left: 0; top: 200px; width: 882px; color: var(--card-white); }
  .card--back .brand-name__main { font-size: 64px; }
  .card--back .brand-name__sub { font-size: 27px; }
</style>
</head>
<body>
<div class="canvas">
  <section class="card card--front">
    <div class="brand-name">
      <span class="brand-name__main">Korvell</span>
      <span class="brand-name__sub">Plant Services</span>
    </div>
    <div class="divider"></div>
    <div class="contact-block">
      <h1 class="person-name">Daniel Hargreave</h1>
      <p class="person-role">Managing Director</p>
      <ul class="contact-list">
        <li class="contact-item">
          <svg class="contact-icon" viewBox="0 0 24 24"><path d="M6.6 10.8a15 15 0 0 0 6.6 6.6l2.2-2.2a1 1 0 0 1 1-.25 11.4 11.4 0 0 0 3.6.57 1 1 0 0 1 1 1V20a1 1 0 0 1-1 1A17 17 0 0 1 3 4a1 1 0 0 1 1-1h3.5a1 1 0 0 1 1 1c0 1.25.2 2.45.57 3.57a1 1 0 0 1-.25 1z"/></svg>
          555-014-2290
        </li>
        <li class="contact-item">
          <svg class="contact-icon" viewBox="0 0 24 24"><path d="M1 4h22v16H1z M3 6v.3l9 6.4 9-6.4V6z M3 8.8V18h18V8.8l-9 6.4z" fill-rule="evenodd"/></svg>
          daniel@korvellplant.com
        </li>
        <li class="contact-item">
          <svg class="contact-icon" viewBox="0 0 24 24"><circle cx="12" cy="12" r="11"/><path d="M1 8.5h22M1 15.5h22M8.5 1v22M15.5 1v22" stroke="#fff" stroke-width="1.6"/></svg>
          www.korvellplant.com
        </li>
      </ul>
    </div>
  </section>

  <section class="card card--back">
    <div class="brand-name">
      <span class="brand-name__main">Korvell</span>
      <span class="brand-name__sub">Plant Services</span>
    </div>
  </section>
</div>
</body>
</html>
```